Australian Civil Construction, Quarry & Mining Services needs a business card

We need a business card designed for our Civil Construction, Quarry & Mining Services based in the country in Australia.
Our Company Brackley Earthworks provide innovate solutions for infrastructure, agricultural and mining (aggregate, sand, roadbase) industry.
We would like our business cards to be double sided
Front of card: black background or something that resembles our business colours. (it doesn't have to be black we are open to options)
- Company name - Brackley Earthworks
- Either our logo or some sort of icon/picture that resembles our business
- Website - https://brackleyearthworks.com.au/
- We will have a number of different names, positions descriptions, phone numbers and emails on separate cards for each of our managers/directors

```html
<!DOCTYPE html>
<html lang="en">
<head>
<meta charset="utf-8">
<title>Brackley Earthworks – Business Card</title>
<link href="https://fonts.googleapis.com/css2?family=Montserrat:wght@500;600;700&display=swap" rel="stylesheet">
<style>
  :root {
    --backdrop: #e4e9e9;
    --card: #0f1012;
    --orange: #ff6600;
    --white: #ffffff;
    --radius: 24px;
  }
  * { margin: 0; padding: 0; box-sizing: border-box; }
  html, body { width: 1083px; height: 1200px; overflow: hidden; }
  body {
    background: var(--backdrop);
    font-family: "Montserrat", Arial, sans-serif;
    position: relative;
  }
  .card {
    position: absolute;
    left: 131px;
    width: 821px;
    height: 469px;
    background: var(--card);
    border-radius: var(--radius);
    overflow: hidden;
  }
  .card--front { top: 81px; }
  .card--back { top: 650px; }

  /* Brand wordmark */
  .brand {
    position: absolute;
    display: flex;
    align-items: center;
    color: var(--orange);
    font-weight: 700;
    letter-spacing: 1px;
    line-height: 1.08;
  }
  .brand__mark {
    background: var(--orange);
    border-radius: 10px;
    flex: none;
  }
  .card--front .brand {
    left: 0; right: 0; top: 146px;
    justify-content: center;
    gap: 26px;
    font-size: 52px;
  }
  .card--front .brand__mark { width: 124px; height: 124px; }
  .card--back .brand {
    left: 30px; width: 320px; top: 190px;
    gap: 18px;
    font-size: 36px;
  }
  .card--back .brand__mark { width: 82px; height: 82px; border-radius: 8px; }

  /* Front web band */
  .web-band {
    position: absolute;
    left: 0; right: 0; top: 407px;
    height: 42px;
    background: var(--orange);
    display: flex;
    align-items: center;
    justify-content: center;
    gap: 11px;
    color: var(--white);
    font-size: 22px;
    font-weight: 500;
    letter-spacing: 2.6px;
  }
  .web-band svg { width: 25px; height: 25px; }

  /* Back details */
  .divider {
    position: absolute;
    left: 373px; top: 82px;
    width: 2px; height: 306px;
    background: var(--orange);
  }
  .person {
    position: absolute;
    left: 417px; top: 113px; right: 0;
    padding-bottom: 6px;
    border-bottom: 2px solid var(--orange);
  }
  .person__name {
    color: var(--orange);
    font-size: 28px;
    font-weight: 700;
    letter-spacing: 3px;
    line-height: 1.1;
  }
  .person__role {
    color: var(--white);
    font-size: 14.5px;
    font-weight: 500;
    letter-spacing: 1.6px;
  }
  .contacts {
    position: absolute;
    left: 417px; top: 224px;
    list-style: none;
  }
  .contacts li {
    display: flex;
    align-items: center;
    height: 33.5px;
    color: var(--white);
    font-size: 16px;
    font-weight: 500;
    letter-spacing: 1.9px;
  }
  .contacts svg {
    width: 18px; height: 18px;
    margin-right: 14px;
    flex: none;
  }
</style>
</head>
<body>

<section class="card card--front" aria-label="Business card front">
  <div class="brand"><span class="brand__mark"></span><span>Brackley<br>Earthworks</span></div>
  <div class="web-band">
    <svg viewBox="0 0 24 24" fill="none" stroke="#fff" stroke-width="1.4">
      <circle cx="12" cy="12" r="10"/>
      <ellipse cx="12" cy="12" rx="4.5" ry="10"/>
      <line x1="2" y1="12" x2="22" y2="12"/>
      <path d="M4 6.5h16M4 17.5h16"/>
    </svg>
    <span>https://brackleyearthworks.com.au</span>
  </div>
</section>

<section class="card card--back" aria-label="Business card back">
  <div class="brand"><span class="brand__mark"></span><span>Brackley<br>Earthworks</span></div>
  <div class="divider"></div>
  <div class="person">
    <p class="person__name">Daniel Orsay</p>
    <p class="person__role">Project Manager</p>
  </div>
  <ul class="contacts">
    <li>
      <svg viewBox="0 0 24 24" fill="none" stroke="#fff" stroke-width="1.3" stroke-linejoin="round">
        <path d="M5 3l3.5 0 1.5 4.5-2.2 1.5a11 11 0 0 0 7.2 7.2l1.5-2.2 4.5 1.5 0 3.5a2 2 0 0 1-2 2A17 17 0 0 1 3 5a2 2 0 0 1 2-2z"/>
        <path d="M14 3a7 7 0 0 1 7 7M14 6.5a3.5 3.5 0 0 1 3.5 3.5"/>
      </svg>
      123-456-7890
    </li>
    <li>
      <svg viewBox="0 0 24 24" fill="none" stroke="#fff" stroke-width="1.3">
        <rect x="2" y="5" width="20" height="14"/>
        <path d="M2 5l10 8 10-8M2 19l7.5-7M22 19l-7.5-7"/>
      </svg>
      info@brackleyearthworks.com.au
    </li>
    <li>
      <svg viewBox="0 0 24 24" fill="none" stroke="#fff" stroke-width="1.3">
        <circle cx="12" cy="12" r="10"/>
        <ellipse cx="12" cy="12" rx="4.5" ry="10"/>
        <line x1="2" y1="12" x2="22" y2="12"/>
        <path d="M4 6.5h16M4 17.5h16"/>
      </svg>
      https://brackleyearthworks.com.au
    </li>
    <li>
      <svg viewBox="0 0 24 24" fill="none" stroke="#fff" stroke-width="1.3">
        <path d="M12 17s-5-5.5-5-9a5 5 0 0 1 10 0c0 3.5-5 9-5 9z"/>
        <circle cx="12" cy="8" r="1.8"/>
        <ellipse cx="12" cy="19.5" rx="7" ry="2.2"/>
      </svg>
      14 Tallow Road, Your Location
    </li>
  </ul>
</section>

</body>
</html>
```